Pharmacy ad

need 2 pharmacy ads for the phone book. one for Birchfield Pharmacy and one for Corvane Rx Pharmacy. Dimensions for ad is 4.75in x 4.667 in. please see attached examples of ad uploaded as well logos of each pharmacy

```html
<!DOCTYPE html>
<html lang="en">
<head>
<meta charset="utf-8">
<title>Corvane Rx Pharmacy – Directory Ad</title>
<link rel="stylesheet" href="https://fonts.googleapis.com/css2?family=Lato:ital,wght@0,300;0,400;0,700;0,900;1,700;1,900&family=Roboto+Condensed:ital,wght@0,300;0,400;0,700;1,700&display=swap">
<style>
  :root {
    --brand-blue: #3a4c9f;
    --brand-green: #6cbf44;
    --page-bg: #eeeeee;
    --panel-white: #ffffff;
    --panel-mist: #ececec;
    --rule-green: #9fd47f;
  }
  * { box-sizing: border-box; margin: 0; padding: 0; }
  html, body { width: 1200px; height: 1000px; overflow: hidden; }
  body { background: var(--page-bg); position: relative; font-family: "Lato", sans-serif; }

  .ad {
    position: absolute; left: 253px; top: 142px; width: 715px; height: 701px;
    background: var(--brand-green); padding: 12px;
  }
  .ad-surface {
    position: relative; width: 100%; height: 100%; overflow: hidden;
    background: radial-gradient(ellipse at 70% 40%, var(--panel-mist) 0%, var(--panel-white) 75%);
  }
  .ad-surface > * { position: absolute; }

  .store-info {
    left: 0; right: 0; top: 14px; text-align: center;
    font-family: "Roboto Condensed", sans-serif; color: var(--brand-blue);
    font-size: 15.5px; line-height: 20.5px; font-weight: 400;
  }
  .store-info .phone { font-family: "Lato", sans-serif; font-weight: 700; font-size: 15px; }

  .brand-name {
    left: 0; right: 0; top: 98px; display: flex; align-items: center; justify-content: center; gap: 18px;
    color: var(--brand-blue); font-weight: 700; font-size: 46px; letter-spacing: -0.5px;
  }
  .brand-name .brand-mark { width: 30px; height: 30px; background: var(--brand-green); }

  .tagline-band { left: 0; top: 204px; width: 668px; height: 86px; }
  .tagline-band svg { position: absolute; inset: 0; }
  .tagline-band h2 {
    position: relative; padding-left: 20px; line-height: 86px;
    color: #fff; font-style: italic; font-weight: 900; font-size: 44px; letter-spacing: 0.2px;
  }

  .service-list {
    list-style: none; font-family: "Roboto Condensed", sans-serif; font-weight: 300;
    color: var(--brand-blue); font-size: 25px;
  }
  .service-list li { display: flex; align-items: center; height: 35.6px; gap: 14px; }
  .service-list svg { width: 28px; height: 26px; flex: none; }
  .services-left { left: 35px; top: 315px; }
  .services-right { left: 283px; top: 315px; }

  .rule { left: 32px; right: 23px; height: 1px; background: var(--rule-green); }
  .rule-top { top: 493px; }
  .rule-bottom { top: 623px; }

  .discount-figure {
    left: 60px; top: 497px; color: var(--brand-blue); font-weight: 900; font-size: 118px; letter-spacing: -3px; line-height: 120px;
  }
  .discount-terms { left: 311px; top: 513px; color: var(--brand-blue); }
  .discount-terms p { font-weight: 900; font-size: 24px; line-height: 34px; }
  .discount-terms .note { font-weight: 400; font-size: 19px; line-height: 22px; }

  .accept-label { left: 33px; top: 642px; color: var(--brand-green); font-weight: 300; font-size: 25px; }
  .accepted-partners {
    left: 172px; top: 651px; display: flex; gap: 14px; align-items: center;
    font-weight: 700; font-size: 11.5px; color: var(--brand-blue);
  }
  .accepted-partners span { display: flex; align-items: center; gap: 4px; }
  .accepted-partners i { width: 8px; height: 8px; background: var(--brand-green); display: inline-block; }

  .social-tab { right: 0; bottom: 0; width: 198px; height: 34px; }
  .social-tab svg { position: absolute; inset: 0; }
  .social-tab p {
    position: relative; text-align: right; padding-right: 12px; line-height: 34px;
    font-family: "Roboto Condensed", sans-serif; font-style: italic; font-weight: 700; font-size: 16px; color: #fff;
  }
</style>
</head>
<body>
  <article class="ad">
    <div class="ad-surface" role="img" aria-label="Soft-focus background of white pills and capsules">
      <header class="store-info">
        <p>Monday – Saturday Thursday 8am- 7pm &nbsp;|&nbsp; Sunday 10am-2pm</p>
        <p>Suite 4, Marlow Court Plaza, Harbour Street, Eastport</p>
        <p class="phone">Phone: 555-0187</p>
      </header>

      <h1 class="brand-name"><span class="brand-mark"></span>Corvane Rx Pharmacy</h1>

      <div class="tagline-band">
        <svg width="668" height="86" viewBox="0 0 668 86" aria-hidden="true"><polygon points="0,0 668,0 633,86 0,86" fill="var(--brand-green)"/></svg>
        <h2>Where Good Health Begins</h2>
      </div>

      <ul class="service-list services-left">
        <li><svg viewBox="0 0 28 26"><path d="M2 14 L10 22 L26 3" fill="none" stroke="var(--brand-blue)" stroke-width="5"/></svg>Affordable prices</li>
        <li><svg viewBox="0 0 28 26"><path d="M2 14 L10 22 L26 3" fill="none" stroke="var(--brand-blue)" stroke-width="5"/></svg>Injectables</li>
        <li><svg viewBox="0 0 28 26"><path d="M2 14 L10 22 L26 3" fill="none" stroke="var(--brand-blue)" stroke-width="5"/></svg>Special Orders</li>
        <li><svg viewBox="0 0 28 26"><path d="M2 14 L10 22 L26 3" fill="none" stroke="var(--brand-blue)" stroke-width="5"/></svg>Delivery service</li>
      </ul>
      <ul class="service-list services-right">
        <li><svg viewBox="0 0 28 26"><path d="M2 14 L10 22 L26 3" fill="none" stroke="var(--brand-blue)" stroke-width="5"/></svg>Certified Pharmacists</li>
        <li><svg viewBox="0 0 28 26"><path d="M2 14 L10 22 L26 3" fill="none" stroke="var(--brand-blue)" stroke-width="5"/></svg>Brand and Generic Medicines</li>
        <li><svg viewBox="0 0 28 26"><path d="M2 14 L10 22 L26 3" fill="none" stroke="var(--brand-blue)" stroke-width="5"/></svg>Blood Pressure and Glucose checks</li>
        <li><svg viewBox="0 0 28 26"><path d="M2 14 L10 22 L26 3" fill="none" stroke="var(--brand-blue)" stroke-width="5"/></svg>Personal care and Beauty Products</li>
      </ul>

      <div class="rule rule-top"></div>

      <p class="discount-figure">10%</p>
      <div class="discount-terms">
        <p>SENIOR CITIZEN DISCOUNT</p>
        <p>STUDENT DISCOUNT</p>
        <p class="note">(With valid ID card)</p>
      </div>

      <div class="rule rule-bottom"></div>

      <p class="accept-label">We accept</p>
      <div class="accepted-partners">
        <span><i></i>Orbicard</span>
        <span>Vantapay</span>
        <span>Selwyn Life</span>
        <span>Harbor Assurance</span>
      </div>

      <div class="social-tab">
        <svg width="198" height="34" viewBox="0 0 198 34" aria-hidden="true"><polygon points="14,0 198,0 198,34 0,34" fill="var(--brand-blue)"/></svg>
        <p>Visit us on Chatterly</p>
      </div>
    </div>
  </article>
</body>
</html>
```